Coupons App Design Project

We have a simple coupons app with few screens and actions:
1. Very simple login screen (with chatterloop and findwell+)
2. Very simple business search page
3. Very simple business search results(each result contains logo icon, business name and delete icon)
4. business list (every row contains logo icon, business name and delete icon)
5. coupons list (each item contains image, title, subtitle, description, expiration time, status graphics (valid, expired, redeemed), delete icon
6. coupon view (image, title, subtitle, description, barcode etc.)
7. custom confirmation dialog(title, buttons, background, text)
8. "scan to subscribe" page (merchant name, merchant number, background image, text, barcode to scan etc.)
9. simple menu
10. splash screen

all graphics should be vector graphics so we can use it to different resolutions including for printing
Updates

Hi all, We've increased the project's budget by 25%. Thanks

Hi all,

We've decided to change the project from refundable to committed payment.
FYI

Hi All,

Thank you for your time and efforts, we really appreciate it.However we've eliminated most of the offered designs we've received becausethey didn't fit our desired look and feel.

Please download our look and feel file from our uploaded files -we've put there some examples of other apps that we like.

Thanks

Target Market(s)

shoppers all over the world

Industry/Entity Type

Business

Requirements
Must have
• Please take a look at the attached file "look & feel.jpg" for some nice screen shots taken from apps that we like

Should not have
• *****************************************************************************************
The attached files are only for demonstration purpose and needs descriptions so please don't send us design based on these screenshots.
*****************************************************************************************

```html
<!DOCTYPE html>
<html lang="en">
<head>
<meta charset="utf-8">
<title>Coupons App – Login and Business Search</title>
<link href="https://fonts.googleapis.com/css2?family=Quicksand:wght@400;500&display=swap" rel="stylesheet">
<style>
  :root {
    --backdrop: #231f20;
    --header-green: #a6d26a;
    --screen-top: #ffffff;
    --screen-bottom: #f1f1f1;
    --text-grey: #777777;
    --rule-grey: #e8e8e8;
    --field-border: #aaaaaa;
    --icon-faint: #e2e2e2;
    --primary-blue: #6a9fcb;
    --secondary-coral: #f5876e;
    --white: #ffffff;
  }
  * { box-sizing: border-box; margin: 0; padding: 0; }
  html, body {
    width: 1200px; height: 891px; overflow: hidden;
    background: var(--backdrop);
    font-family: "Quicksand", sans-serif;
  }
  .stage {
    position: absolute; left: 0; top: 0;
    width: 1120px; height: 832px;
    transform: scale(1.0714, 1.0709);
    transform-origin: 0 0;
  }
  .screen {
    position: absolute; width: 515px;
    background: linear-gradient(to bottom, var(--screen-top) 55%, var(--screen-bottom));
    overflow: hidden;
  }
  .screen--login { left: 16px; top: 25px; height: 781px; }
  .screen--search { left: 580px; top: 25px; height: 773px; }
  .app-bar {
    position: relative; background: var(--header-green);
    color: var(--white); text-align: center;
  }
  .screen--login .app-bar { height: 87px; }
  .screen--search .app-bar { height: 79px; }
  .app-bar__title {
    position: absolute; left: 0; right: 0; top: 50%;
    transform: translateY(-52%);
    font-size: 33px; font-weight: 400; letter-spacing: 0.2px;
  }
  .app-bar__icon { position: absolute; top: 50%; width: 56px; height: 56px; margin-top: -28px; }
  .app-bar__icon--back { left: 16px; }
  .app-bar__icon--settings { right: 12px; }
  .screen--search .app-bar__icon--settings { right: 11px; }

  .rule { position: absolute; height: 3px; background: var(--rule-grey); }
  .centered { position: absolute; left: 0; right: 0; text-align: center; color: var(--text-grey); font-weight: 400; }

  .login-title { top: 132px; font-size: 36px; }
  .login-rule-top { left: 19px; right: 19px; top: 205px; }
  .login-intro { top: 233px; font-size: 21px; line-height: 30.5px; }
  .login-rule-bottom { left: 19px; right: 19px; top: 347px; }
  .login-button {
    position: absolute; left: 27px; width: 452px; height: 86px;
    border-radius: 16px; color: var(--white);
    font-size: 34px; display: flex; align-items: center; justify-content: center;
    box-shadow: 0 2px 4px rgba(0,0,0,0.12);
  }
  .login-button--primary { top: 434px; background: var(--primary-blue); }
  .login-button--secondary { top: 537px; background: var(--secondary-coral); }

  .session-note { top: 87px; font-size: 17px; }
  .search-rule { left: 19px; right: 19px; top: 118px; }
  .search-title { top: 152px; font-size: 37px; }
  .search-field {
    position: absolute; left: 55px; top: 218px; width: 436px; height: 50px;
    border: 3px solid var(--field-border); background: var(--white);
  }
  .search-field__placeholder {
    position: absolute; left: 17px; top: 10px; font-size: 18px; color: var(--text-grey);
  }
  .search-field__icon { position: absolute; right: 10px; top: 6px; width: 34px; height: 34px; }
  .search-help { top: 303px; font-size: 17px; line-height: 24px; }
</style>
</head>
<body>
<main class="stage">

  <section class="screen screen--login">
    <header class="app-bar">
      <svg class="app-bar__icon app-bar__icon--back" viewBox="0 0 56 56" aria-label="Back">
        <circle cx="28" cy="28" r="25" fill="none" stroke="#fff" stroke-width="3.5"/>
        <circle cx="28" cy="28" r="13" fill="#fff"/>
        <path d="M34 28H22M27 22l-6 6 6 6" fill="none" stroke="#a6d26a" stroke-width="3.5" stroke-linecap="round" stroke-linejoin="round"/>
      </svg>
      <h1 class="app-bar__title">Coupons App</h1>
      <svg class="app-bar__icon app-bar__icon--settings" viewBox="0 0 56 56" aria-label="Settings">
        <circle cx="28" cy="28" r="25" fill="none" stroke="#fff" stroke-width="3.5"/>
        <g fill="#fff">
          <circle cx="28" cy="28" r="11"/>
          <rect x="25" y="13" width="6" height="30" rx="1"/>
          <rect x="25" y="13" width="6" height="30" rx="1" transform="rotate(45 28 28)"/>
          <rect x="25" y="13" width="6" height="30" rx="1" transform="rotate(90 28 28)"/>
          <rect x="25" y="13" width="6" height="30" rx="1" transform="rotate(135 28 28)"/>
        </g>
        <circle cx="28" cy="28" r="5" fill="#a6d26a"/>
      </svg>
    </header>

    <h2 class="centered login-title">Login</h2>
    <div class="rule login-rule-top"></div>
    <p class="centered login-intro">Sign in to the coupon app<br>and start working and<br>some sample text . . .</p>
    <div class="rule login-rule-bottom"></div>

    <div class="login-button login-button--primary">Login with chatterloop</div>
    <div class="login-button login-button--secondary">Login with findwell</div>
  </section>

  <section class="screen screen--search">
    <header class="app-bar">
      <svg class="app-bar__icon app-bar__icon--back" viewBox="0 0 56 56" aria-label="Back">
        <circle cx="28" cy="28" r="25" fill="none" stroke="#fff" stroke-width="3.5"/>
        <circle cx="28" cy="28" r="13" fill="#fff"/>
        <path d="M34 28H22M27 22l-6 6 6 6" fill="none" stroke="#a6d26a" stroke-width="3.5" stroke-linecap="round" stroke-linejoin="round"/>
      </svg>
      <h1 class="app-bar__title">Coupons App</h1>
      <svg class="app-bar__icon app-bar__icon--settings" viewBox="0 0 56 56" aria-label="Settings">
        <circle cx="28" cy="28" r="25" fill="none" stroke="#fff" stroke-width="3.5"/>
        <g fill="#fff">
          <circle cx="28" cy="28" r="11"/>
          <rect x="25" y="13" width="6" height="30" rx="1"/>
          <rect x="25" y="13" width="6" height="30" rx="1" transform="rotate(45 28 28)"/>
          <rect x="25" y="13" width="6" height="30" rx="1" transform="rotate(90 28 28)"/>
          <rect x="25" y="13" width="6" height="30" rx="1" transform="rotate(135 28 28)"/>
        </g>
        <circle cx="28" cy="28" r="5" fill="#a6d26a"/>
      </svg>
    </header>

    <p class="centered session-note">Logged in as Sample Name</p>
    <div class="rule search-rule"></div>
    <h2 class="centered search-title">Business Search</h2>

    <div class="search-field">
      <span class="search-field__placeholder">Tap here to edit text&nbsp; . . .</span>
      <svg class="search-field__icon" viewBox="0 0 34 34" aria-label="Search">
        <circle cx="14" cy="14" r="9" fill="none" stroke="#e2e2e2" stroke-width="4"/>
        <path d="M21 21l9 9" stroke="#e2e2e2" stroke-width="6" stroke-linecap="round"/>
      </svg>
    </div>

    <p class="centered search-help">You can search businesses by name<br>etc and some sample text<br>comes here . . .</p>
  </section>

</main>
</body>
</html>
```